New site for parent-to-parent advice in spanish requieres Wordpress design

Crianzaluz.com ("time for child" in spanish) is a web site dedicated to give support from father to father in order to attend small babies and childs. The core idea is that divorced, single or widow male parents can get advice from other parents on attending our kids alone, as for short term visits or as single parents. It must be fun and easy to navigate, simple, practical and male-oriented. The site will be in spanish and Mexico and Latin-america market. Some subcategories will be ages of kids (toddlers, kids, preadolescents, adolescents; Bebés, Niños, Preadolescentes, Adolescentes) and other will be the father situation (widows, singles, divorced or even married; Viudos, Solteros, Divorciados, Casados).
Updates

Project Deadline Extended
Reason: As some of your questions are if it includes Wordpress Code and the answer is yes, we are recibed request to extend the deadline to workdays in order to can get the code over an unpdated designs. Thanks.

Target Market(s)

Divorced, single or widow male parents can get advice from other parents on attending our kids alone, as for short term visits or as single parents. The site will be in spanish an Latin-America oriented.

Industry/Entity Type

It Support

Requirements
Must have
• Crianzaluz.com as the name of the site.
Space for banners well identified, in order to sell publicity but to clearly states wich is advice from the team and what paid publicity.
Nice to have
• Penguins will be prefered as the site mascot or graphic elements, since Penguins are the only animal in which male parent keep in charge of the small ones alone for six months a year -view photo for reference, not necesarly for direct use-
Trinos and Redvecina buttons.

```html
<!DOCTYPE html>
<html lang="es">
<head>
<meta charset="utf-8">
<title>Crianzaluz.com</title>
<link rel="stylesheet" href="https://fonts.googleapis.com/css2?family=Bebas+Neue&family=Chewy&family=Noto+Sans:wght@400;700&display=swap">
<style>
:root{
  --sky-top:#a6dcf3;
  --sky-bottom:#7fc4e6;
  --nav:#2f7ea2;
  --nav-dark:#1f6283;
  --active:#2a2f35;
  --cream:#fdf5e2;
  --tips:#6498b1;
  --side-head:#2f7ea2;
  --side-list:#58a6ca;
  --footer:#232b33;
  --ink:#2b2b2b;
  --white:#ffffff;
  --social-a:#2d5fa6;
  --social-b:#3fb1e3;
  --ad-blue:#3b5998;
}
*{box-sizing:border-box;margin:0;padding:0}
html,body{width:969px;height:1200px;overflow:hidden}
body{background:var(--cream);font-family:"Noto Sans",sans-serif;color:var(--ink);position:relative}
.wrap{width:570px;margin:0 auto;position:relative}

.site-header{height:100px;background:linear-gradient(var(--sky-top),var(--sky-bottom))}
.site-header .wrap{height:100px}
.brand{position:absolute;left:0;top:22px;display:flex;align-items:center;gap:8px;white-space:nowrap}
.brand-dot{width:50px;height:50px;border-radius:50%;background:var(--nav-dark);flex:none}
.brand-name{font-family:"Bebas Neue",sans-serif;font-size:26px;color:var(--nav-dark);letter-spacing:.5px}
.tagline{position:absolute;left:215px;top:30px;font-family:"Bebas Neue",sans-serif;font-size:19px;line-height:22px;color:var(--white);letter-spacing:.5px;white-space:nowrap}
.social{position:absolute;right:0;top:32px;display:flex;gap:3px}
.social-btn{width:40px;height:40px;display:flex;align-items:center;justify-content:center;font-family:"Noto Sans",sans-serif;font-size:7px;color:var(--white)}
.social-btn.red{background:var(--social-a)}
.social-btn.trinos{background:var(--social-b)}

.main-nav{height:29px;background:var(--nav);border-top:1px solid var(--nav-dark);border-bottom:1px solid var(--nav-dark)}
.main-nav ul{list-style:none;display:flex;justify-content:center;height:100%}
.main-nav li{font-family:"Bebas Neue",sans-serif;font-size:15px;color:var(--white);padding:0 11px;display:flex;align-items:center;position:relative;letter-spacing:.3px;white-space:nowrap}
.main-nav li+li::before{content:"";position:absolute;left:-2px;top:12px;width:4px;height:4px;border-radius:50%;background:var(--white)}
.main-nav li.active{background:var(--active)}

.tips-bar{position:absolute;left:200px;top:137px;width:570px;height:70px;background:var(--tips)}
.tips-label{position:absolute;left:6px;top:-4px;background:var(--cream);padding:0 4px;font-family:"Bebas Neue",sans-serif;font-size:26px;color:var(--ink);line-height:28px}
.tips-arrows{position:absolute;right:6px;top:-3px;display:flex}
.tips-arrows span{width:15px;height:18px;background:var(--cream);border:1px solid #8a8a8a;display:flex;align-items:center;justify-content:center}
.tips-text{position:absolute;left:14px;right:14px;top:30px;text-align:center;font-style:italic;font-size:10px;line-height:14px;color:var(--white)}

.content{position:absolute;left:200px;top:221px;width:376px}
.ad-banner{height:55px;background:var(--white);border:1px solid #d6d6d6}
.ad-banner .ad-head{height:18px;background:var(--ad-blue);color:var(--white);font-weight:700;font-size:12px;padding-left:8px;line-height:18px}
.ad-banner .ad-body{display:flex;align-items:center;height:35px;padding:0 8px;font-size:11px;white-space:nowrap}
.ad-banner strong{margin-right:8px}
.ad-banner .ad-link{color:var(--ad-blue)}
.ad-banner .ad-btn{margin-left:auto;background:#5b9a3a;color:var(--white);font-size:9px;padding:3px 8px;border-radius:2px}
.section-title{font-family:"Bebas Neue",sans-serif;font-weight:400;font-size:22px;margin:12px 0 6px;letter-spacing:.5px}
.person{height:139px;font-size:10px;line-height:14.5px}
.person-photo{float:left;width:84px;height:84px;margin:0 14px 4px 0}
.person p+p{margin-top:14px}
.content .ad-banner.bottom{position:absolute;top:671px;width:376px}

.sidebar{position:absolute;left:587px;top:221px;width:183px}
.side-block h3{background:var(--side-head);font-family:"Chewy",sans-serif;font-weight:400;font-size:20px;color:var(--white);height:36px;line-height:36px;padding-left:11px;white-space:nowrap;overflow:hidden}
.side-block ul{background:var(--side-list);padding:4px 0 6px 32px;list-style:disc;color:var(--white)}
.side-block li{font-size:11px;line-height:18px}
.side-ad-wrap{position:relative}
.side-ad{margin-top:6px;height:152px;background:var(--white);border:1px solid #c9c9c9;padding:6px;text-align:center}
.side-ad .ad-title{font-size:15px;color:#2372c4;line-height:18px;letter-spacing:-.5px;white-space:nowrap}
.side-ad .ad-sub{font-size:8px;color:#d33;line-height:9px;margin-top:2px}
.side-ad .ad-offer{font-size:11px;color:#2372c4;line-height:13px;margin-top:8px}
.side-ad .ad-photo{position:absolute;left:13px;top:98px;width:70px;height:42px;background:linear-gradient(135deg,#c9a36a,#7a5a3a)}
.side-ad .ad-cta{position:absolute;right:12px;top:104px;background:#f08a2a;color:var(--white);font-size:9px;padding:5px 8px;border-radius:10px}

.footer-nav{position:absolute;top:964px;left:0;width:969px;height:29px;background:var(--nav)}
.site-footer{position:absolute;top:993px;left:0;width:969px;height:207px;background:var(--footer);color:var(--white)}
.footer-col{position:absolute;top:14px}
.footer-col h4{font-family:"Bebas Neue",sans-serif;font-weight:400;font-size:12px;letter-spacing:.3px;margin:0 0 5px}
.footer-col ul{list-style:disc;padding-left:26px;margin-bottom:10px}
.footer-col li{font-size:8px;line-height:12px}
.footer-social{display:flex;gap:3px;margin-top:6px}
.footer-social .social-btn{width:38px;height:38px}
.footer-brand{position:absolute;left:603px;top:26px;display:flex;align-items:center;gap:10px;white-space:nowrap}
.footer-brand .brand-dot{background:var(--nav)}
.footer-brand .brand-name{color:var(--white)}
.legal{position:absolute;top:180px;left:0;width:100%;text-align:center;font-size:8px;line-height:11px}
.legal span{margin:0 6px}
</style>
</head>
<body>
<header class="site-header">
  <div class="wrap">
    <div class="brand"><span class="brand-dot"></span><span class="brand-name">Crianzaluz.com</span></div>
    <p class="tagline">Lorem ipsum dolor sit amet,<br>consectetur adipiscing elit. Phasellus</p>
    <div class="social"><span class="social-btn red">Redvecina</span><span class="social-btn trinos">Trinos</span></div>
  </div>
</header>
<nav class="main-nav">
  <ul>
    <li>Inicio</li><li>Primeros Pasos</li><li>Padre a Padre</li><li class="active">Hijos por Edades</li><li>Situacion del Padre</li><li>Nosotros</li><li>Contactos</li>
  </ul>
</nav>

<section class="tips-bar">
  <span class="tips-label">Tips!</span>
  <div class="tips-arrows">
    <span><svg width="6" height="8"><path d="M5 0L0 4L5 8Z" fill="#333"/></svg></span>
    <span><svg width="6" height="8"><path d="M1 0L6 4L1 8Z" fill="#333"/></svg></span>
  </div>
  <p class="tips-text">Lorem ipsum dolor sit amet, consectetur adipiscing elit. Vivamus nec sodales ligula. Aenean tincidunt vitae ante eget faucibus. Vivamus ac diam diam. Sed ac sapien cursus diam sagittis consequat sit amet sit amet lectus.</p>
</section>

<main class="content">
  <div class="ad-banner">
    <div class="ad-head">Redvecina</div>
    <div class="ad-body"><strong>Create a Redvecina profile</strong><span class="ad-link">Sign up for free today!</span><span class="ad-btn">Sign Up</span></div>
  </div>
  <h2 class="section-title">Nosotros</h2>
  <article class="person">
    <div class="person-photo" role="img" aria-label="Foto de miembro del equipo" style="background:linear-gradient(#e9e4df,#b98f7c)"></div>
    <p><strong>Lorem ipsum dolor</strong> sit amet, consectetur adipiscing elit. Vivamus nec sodales ligula. Aenean tincidunt vitae ante eget faucibus. Vivamus ac diam diam. Sed ac sapien cursus diam sagittis consequat sit amet sit amet lectus.</p>
    <p>Lorem ipsum dolor sit amet, consectetur adipiscing elit. Vivamus nec sodales ligula. Aenean tincidunt vitae ante eget faucibus. Vivamus ac diam diam. Sed ac sapien cursus diam sagittis consequat sit amet sit amet lectus.</p>
  </article>
  <article class="person">
    <div class="person-photo" role="img" aria-label="Foto de miembro del equipo" style="background:linear-gradient(#8a97a6,#3c4350)"></div>
    <p><strong>Lorem ipsum dolor</strong> sit amet, consectetur adipiscing elit. Vivamus nec sodales ligula. Aenean tincidunt vitae ante eget faucibus. Vivamus ac diam diam. Sed ac sapien cursus diam sagittis consequat sit amet sit amet lectus.</p>
    <p>Lorem ipsum dolor sit amet, consectetur adipiscing elit. Vivamus nec sodales ligula. Aenean tincidunt vitae ante eget faucibus. Vivamus ac diam diam. Sed ac sapien cursus diam sagittis consequat sit amet sit amet lectus.</p>
  </article>
  <article class="person">
    <div class="person-photo" role="img" aria-label="Foto de miembro del equipo" style="background:linear-gradient(#c7d3dc,#3a3e46)"></div>
    <p><strong>Lorem ipsum dolor</strong> sit amet, consectetur adipiscing elit. Vivamus nec sodales ligula. Aenean tincidunt vitae ante eget faucibus. Vivamus ac diam diam. Sed ac sapien cursus diam sagittis consequat sit amet sit amet lectus.</p>
    <p>Lorem ipsum dolor sit amet, consectetur adipiscing elit. Vivamus nec sodales ligula. Aenean tincidunt vitae ante eget faucibus. Vivamus ac diam diam. Sed ac sapien cursus diam sagittis consequat sit amet sit amet lectus.</p>
  </article>
  <article class="person">
    <div class="person-photo" role="img" aria-label="Foto de miembro del equipo" style="background:linear-gradient(#e9e4df,#b98f7c)"></div>
    <p><strong>Lorem ipsum dolor</strong> sit amet, consectetur adipiscing elit. Vivamus nec sodales ligula. Aenean tincidunt vitae ante eget faucibus. Vivamus ac diam diam. Sed ac sapien cursus diam sagittis consequat sit amet sit amet lectus.</p>
    <p>Lorem ipsum dolor sit amet, consectetur adipiscing elit. Vivamus nec sodales ligula. Aenean tincidunt vitae ante eget faucibus. Vivamus ac diam diam. Sed ac sapien cursus diam sagittis consequat sit amet sit amet lectus.</p>
  </article>
  <div class="ad-banner bottom">
    <div class="ad-head">Redvecina</div>
    <div class="ad-body"><strong>Create a Redvecina profile</strong><span class="ad-link">Sign up for free today!</span><span class="ad-btn">Sign Up</span></div>
  </div>
</main>

<aside class="sidebar">
  <section class="side-block"><h3>Primeros Pasos</h3><ul><li>Lorem Ipsum</li><li>Dolor sit amet</li><li>Consectetur</li><li>Adipiscing elit</li></ul></section>
  <section class="side-block"><h3>Padre a Padre</h3><ul><li>Lorem Ipsum</li><li>Dolor sit amet</li><li>Consectetur</li><li>Adipiscing elit</li></ul></section>
  <section class="side-block"><h3>Hijos por Edades</h3><ul><li>Bebés</li><li>Niños</li><li>Preadolescentes</li><li>Adolescentes</li></ul></section>
  <section class="side-block"><h3>Situacion del Padre</h3><ul><li>Viudos</li><li>Solteros</li><li>Divorciados</li><li>Casados</li></ul></section>
  <section class="side-block"><h3>Tips</h3></section>
  <div class="side-ad-wrap">
    <div class="side-ad">
      <p class="ad-title">Apartamentos Temporales</p>
      <p class="ad-sub">EL MEJOR PRECIO EN LOS<br>MEJORES APARTAMENTOS</p>
      <p class="ad-offer">LAS MEJORES OFERTAS EN<br>TEMPORADA ALTA</p>
      <div class="ad-photo" role="img" aria-label="Foto de interior de apartamento"></div>
      <span class="ad-cta">INFÓRMESE YA</span>
    </div>
  </div>
</aside>

<nav class="main-nav footer-nav">
  <ul>
    <li>Inicio</li><li>Primeros Pasos</li><li>Padre a Padre</li><li>Hijos por Edades</li><li>Situacion del Padre</li><li>Nosotros</li><li>Contactos</li>
  </ul>
</nav>
<footer class="site-footer">
  <div class="footer-col" style="left:200px">
    <h4>Inicio</h4>
    <h4>Primeros Pasos</h4>
    <ul><li>Lorem Ipsum</li><li>Dolor sit amet</li><li>Consectetur</li><li>Adipiscing elit</li></ul>
    <h4>Padre a Padre</h4>
    <ul><li>Lorem Ipsum</li><li>Dolor sit amet</li><li>Consectetur</li><li>Adipiscing elit</li></ul>
  </div>
  <div class="footer-col" style="left:344px">
    <h4>Hijos por Edades</h4>
    <ul><li>Bebés</li><li>Niños</li><li>Preadolescentes</li><li>Adolescentes</li></ul>
    <h4>Situacion del Padre</h4>
    <ul><li>Viudos</li><li>Solteros</li><li>Divorciados</li><li>Casados</li></ul>
  </div>
  <div class="footer-col" style="left:489px">
    <h4>Nosotros</h4>
    <h4>Contactos</h4>
    <div class="footer-social"><span class="social-btn red">Redvecina</span><span class="social-btn trinos">Trinos</span></div>
  </div>
  <div class="footer-brand"><span class="brand-dot"></span><span class="brand-name">Crianzaluz.com</span></div>
  <div class="legal">
    <p><span>Terms and Conditions</span><span>Privacy Policy</span><span>How It Works</span><span>Acceptable Use Policy</span></p>
    <p>© 2013 Crianzaluz.com. Develop by Estudio Nube. All rights reserved.</p>
  </div>
</footer>
</body>
</html>
```